Rack Card for Portuguese Walking Food Tour

I would like a vertical rack card measuring 99x210mm. Here is the information I would like to include. It does not need to be in this format. We are located in Setubal, Portugal.
Please use the attached Teal Heron Logo.
Setúbal: Tradition and Today
Experience the culinary delights of Setúbal, Portugal with a walking food tour around our waterfront village. Discover the Mercado da Gaivota Branca, voted one of the world’s best markets by Metro Ledger, and indulge in local wines and dishes. Prepare for a calm stroll on flat streets. No hills to climb on this tour.
Duration: 4 hours
www.brinebasketwalks.com
+351 265 000 487

```html
<!DOCTYPE html>
<html lang="en">
<head>
<meta charset="utf-8">
<title>Walking Food Tour – Rack Card</title>
<link href="https://fonts.googleapis.com/css2?family=Alfa+Slab+One&family=Arvo:wght@400;700&family=Roboto+Condensed:wght@700&family=Playfair+Display&display=swap" rel="stylesheet">
<style>
  :root {
    --stage: #4a4a4a;
    --orange: #f26a35;
    --orange-deep: #d4472b;
    --orange-ghost: rgba(190, 60, 30, 0.35);
    --cream: #fdf1e6;
    --cream-light: #fffaf5;
    --ink: #5a5a5a;
    --ink-dark: #4f4f4f;
    --white: #ffffff;
  }
  * { margin: 0; padding: 0; box-sizing: border-box; }
  html, body { width: 1200px; height: 1137px; overflow: hidden; }
  body { background: var(--stage); position: relative; }

  .rack-card {
    position: absolute; top: 78px; width: 453px; height: 960px;
    background: linear-gradient(180deg, var(--cream) 0%, var(--cream-light) 100%);
    overflow: hidden;
    box-shadow: 0 14px 14px -8px rgba(0,0,0,0.55);
  }
  .rack-card--front { left: 92px; }
  .rack-card--back { left: 655px; }

  .card-backdrop { position: absolute; left: 0; top: 0; width: 453px; }

  .ghost-title {
    position: absolute; left: 0; top: -6px; width: 453px;
    font-family: "Alfa Slab One", serif; color: var(--orange-ghost);
    text-align: center; line-height: 0.9;
  }
  .ghost-title span { display: block; }
  .ghost-title .g1 { font-size: 70px; letter-spacing: 2px; }
  .ghost-title .g2 { font-size: 132px; }
  .ghost-title .g3 { font-size: 132px; }

  .headline {
    position: absolute; left: 0; top: 20px; width: 453px;
    font-family: "Alfa Slab One", serif; color: var(--white);
    text-align: center; line-height: 1;
    text-shadow: 2px 3px 4px rgba(0,0,0,0.35);
  }
  .headline span { display: block; }
  .headline .h-walking { font-size: 50px; letter-spacing: 1px; }
  .headline .h-food { font-size: 94px; margin-top: 4px; letter-spacing: 1px; }
  .headline .h-tour { font-size: 94px; margin-top: -8px; margin-left: -14px; letter-spacing: 1px; }

  .photo {
    position: absolute; border-radius: 50%;
    border: 6px solid var(--white);
    box-shadow: 0 2px 6px rgba(0,0,0,0.25);
  }
  .photo-shadow {
    position: absolute; height: 10px; border-radius: 50%;
    background: radial-gradient(ellipse at center, rgba(0,0,0,0.45) 0%, rgba(0,0,0,0) 70%);
  }
  .photo--fish { left: 106px; top: 229px; width: 260px; height: 260px;
    background: radial-gradient(circle at 40% 40%, #f4b59a 0%, #e0745a 45%, #b8412f 100%); }
  .photo--platter { left: 22px; top: 239px; width: 206px; height: 206px;
    background: radial-gradient(circle at 60% 35%, #f3e2b9 0%, #d9a866 45%, #8e3e3a 100%); }
  .photo--sign { left: 227px; top: 301px; width: 206px; height: 206px;
    background: linear-gradient(160deg, #c9d6e3 0%, #d262a4 35%, #5b5a5e 70%, #8f8f8f 100%); }
  .photo--oysters { left: 22px; top: 473px; width: 206px; height: 206px;
    background: radial-gradient(circle at 45% 50%, #b7b2a2 0%, #e6e8ea 50%, #cfd2d6 100%); }
  .photo--market { left: 227px; top: 532px; width: 206px; height: 206px;
    background: linear-gradient(180deg, #6d6a5a 0%, #c9a97a 40%, #a57d55 75%, #6e2a34 100%); }

  .spark { position: absolute; }

  .highlights {
    position: absolute; left: 26px; top: 518px; width: 408px;
    font-family: "Arvo", serif; font-size: 16.6px; line-height: 22.8px;
    color: var(--ink); list-style: none; text-align: justify;
  }
  .highlights li { position: relative; padding-left: 20px; }
  .highlights li::before {
    content: "•"; position: absolute; left: 0; top: 0; font-size: 12px; color: var(--ink);
  }

  .duration {
    position: absolute; left: 134px; top: 721px; width: 186px; height: 32px;
    background: var(--orange); color: var(--white);
    font-family: "Arvo", serif; font-weight: 700; font-size: 17px;
    display: flex; align-items: center; justify-content: center;
    transform: skewX(-3deg);
  }
  .duration span { transform: skewX(3deg); }

  .brand {
    position: absolute; left: 0; top: 790px; width: 453px;
    display: flex; align-items: center; justify-content: center; gap: 12px;
  }
  .brand-dot { width: 40px; height: 40px; border-radius: 50%; background: var(--orange); }
  .brand-name {
    font-family: "Arvo", serif; font-weight: 700; font-size: 26px; color: var(--ink-dark);
  }

  .phone {
    position: absolute; left: 0; top: 870px; width: 453px;
    display: flex; align-items: center; justify-content: center; gap: 6px;
    font-family: "Roboto Condensed", sans-serif; font-weight: 700; font-size: 27px;
    color: var(--orange); letter-spacing: 0.5px;
  }
  .phone svg { width: 26px; height: 26px; }

  .website {
    position: absolute; left: 39px; top: 909px; width: 374px; height: 27px;
    border: 1.5px solid var(--ink);
    display: flex; align-items: center; justify-content: center;
    font-family: "Playfair Display", serif; font-size: 14px; letter-spacing: 5.6px;
    color: var(--ink);
  }
  .website .domain { color: var(--orange); }
</style>
</head>
<body>

<!-- FRONT SIDE -->
<article class="rack-card rack-card--front">
  <svg class="card-backdrop" viewBox="0 0 453 480" height="480" aria-hidden="true">
    <defs>
      <linearGradient id="heatFront" x1="0" y1="0" x2="0" y2="1">
        <stop offset="0" stop-color="#f26a35"/>
        <stop offset="1" stop-color="#d4472b"/>
      </linearGradient>
    </defs>
    <path fill="url(#heatFront)" d="M0 0H453V455l-6 -8 -4 14 -8 -10 -10 12 -6 -6 -12 10 -14 -4 -10 12 -8 -6 -10 16 -6 -24 -10 8 -8 -12 -14 6 -20 -4 -30 10 -70 -6 -30 4 -22 -10 -14 6 -10 -10 -12 8 -16 -12 -10 14 -10 -8 -16 12 -8 -10 -12 20 -8 -16 -8 6 -6 -14 -8 6 -6 -16 -6 10 -4 -14z"/>
    <path fill="#d4472b" d="M280 470l4 22 4 -22zM292 472l3 18 3 -18zM310 455l3 14 3 -14z"/>
  </svg>
  <div class="ghost-title" aria-hidden="true"><span class="g1">WALKING</span><span class="g2">FOOD</span><span class="g3">TOUR</span></div>
  <h1 class="headline"><span class="h-walking">WALKING</span><span class="h-food">FOOD</span><span class="h-tour">TOUR</span></h1>

  <svg class="spark" style="left:60px;top:385px" width="50" height="40" viewBox="0 0 50 40" aria-hidden="true">
    <path fill="#fff" d="M2 35L34 28 28 10z"/><path fill="#fff" d="M28 0L44 22 38 2z"/>
  </svg>
  <svg class="spark" style="left:352px;top:424px" width="50" height="40" viewBox="0 0 50 40" aria-hidden="true">
    <path fill="#fff" d="M8 12L42 2 40 26z"/><path fill="#fff" d="M0 18L20 36 8 30z"/>
  </svg>

  <div class="photo photo--fish" role="img" aria-label="Photo of fresh red mullet piled on a fish market stall"></div>
  <div class="photo-shadow" style="left:150px;top:494px;width:170px"></div>

  <ul class="highlights">
    <li>Experience the culinary delights of Setúbal, Portugal with a walking food tour around our waterfront village.</li>
    <li>Discover the Mercado da Gaivota Branca, voted one of the world’s best markets by Metro Ledger, and indulge in local wines and dishes.</li>
    <li>Prepare for a calm stroll on flat streets. No hills to climb on this tour.</li>
  </ul>

  <div class="duration"><span>Duration: 4 hours</span></div>

  <div class="brand"><span class="brand-dot"></span><span class="brand-name">Brine Basket Walks</span></div>

  <p class="phone">
    <svg viewBox="0 0 26 26" aria-hidden="true"><circle cx="13" cy="13" r="11.5" fill="none" stroke="#5a5a5a" stroke-width="1.6"/><path fill="#5a5a5a" d="M9 7.5l2 -0.5 1.3 3 -1.3 1.2c.7 1.6 1.8 2.7 3.3 3.4l1.2 -1.3 3 1.3 -.5 2c-4.6.4 -9.4 -4.4 -9 -9.1z"/></svg>
    +351 265 000 487
  </p>

  <p class="website">www.<span class="domain">brinebasketwalks</span>.com</p>
</article>

<!-- BACK SIDE -->
<article class="rack-card rack-card--back">
  <svg class="card-backdrop" viewBox="0 0 453 730" height="730" aria-hidden="true">
    <defs>
      <linearGradient id="heatBack" x1="0" y1="0" x2="0" y2="1">
        <stop offset="0" stop-color="#f26a35"/>
        <stop offset="1" stop-color="#d4472b"/>
      </linearGradient>
    </defs>
    <path fill="url(#heatBack)" d="M0 0H453V688l-6 -6 -8 12 -12 -8 -10 14 -20 -4 -60 8 -40 -6 -30 4 -20 -6 -40 4 -30 -8 -40 6 -30 -4 -20 8 -14 -10 -10 6 -10 -14 -8 8 -8 -14 -6 10 -8 -14 -6 12 -8 -16 -6 8 -4 -12z"/>
  </svg>
  <div class="ghost-title" aria-hidden="true"><span class="g1">WALKING</span><span class="g2">FOOD</span><span class="g3">TOUR</span></div>
  <h1 class="headline"><span class="h-walking">WALKING</span><span class="h-food">FOOD</span><span class="h-tour">TOUR</span></h1>

  <svg class="spark" style="left:222px;top:275px" width="46" height="42" viewBox="0 0 46 42" aria-hidden="true">
    <path fill="#fff" d="M4 4L14 40 20 16z"/><path fill="#fff" d="M24 30L44 22 36 12z"/>
  </svg>
  <svg class="spark" style="left:20px;top:448px" width="50" height="44" viewBox="0 0 50 44" aria-hidden="true">
    <path fill="#fff" d="M2 24L40 14 12 42z"/><path fill="#fff" d="M20 2L44 14 26 14z"/>
  </svg>
  <svg class="spark" style="left:392px;top:508px" width="50" height="46" viewBox="0 0 50 46" aria-hidden="true">
    <path fill="#fff" d="M2 20L42 14 44 44z"/><path fill="#fff" d="M14 12L36 0 28 14z"/>
  </svg>

  <div class="photo photo--platter" role="img" aria-label="Photo of a board with sliced sausage, cheese and toasted bread"></div>
  <div class="photo-shadow" style="left:50px;top:450px;width:150px"></div>
  <div class="photo photo--sign" role="img" aria-label="Photo of a large town sign with a pink heart in a city square"></div>
  <div class="photo-shadow" style="left:255px;top:512px;width:150px"></div>
  <div class="photo photo--oysters" role="img" aria-label="Photo of fresh oysters on crushed ice with lemon wedges"></div>
  <div class="photo-shadow" style="left:50px;top:684px;width:150px"></div>
  <div class="photo photo--market" role="img" aria-label="Photo of sacks of dried beans and grains at a market stall"></div>
  <div class="photo-shadow" style="left:255px;top:743px;width:150px"></div>

  <div class="brand"><span class="brand-dot"></span><span class="brand-name">Brine Basket Walks</span></div>

  <p class="phone">
    <svg viewBox="0 0 26 26" aria-hidden="true"><circle cx="13" cy="13" r="11.5" fill="none" stroke="#5a5a5a" stroke-width="1.6"/><path fill="#5a5a5a" d="M9 7.5l2 -0.5 1.3 3 -1.3 1.2c.7 1.6 1.8 2.7 3.3 3.4l1.2 -1.3 3 1.3 -.5 2c-4.6.4 -9.4 -4.4 -9 -9.1z"/></svg>
    +351 265 000 487
  </p>

  <p class="website">www.<span class="domain">brinebasketwalks</span>.com</p>
</article>

</body>
</html>
```